Owen Talvik actor business cards

I need unique and interesting business cards that have my headshot photo, my name, tagline/position/skills, contact info, preferred pronouns (he, him, his), and social media handles. These need to be memorable networking tools to hand out at events that stand out. I am an actor that works in theatre, film, and TV and usually play darker dramatic roles, though it doesn't have to necessarily need to be reflected in the design, but I am not a light, comedic actor. In my email tagline, My position/skills are "Actor, storyteller, theatre maker."

Target Market(s)

Casting directors, film and television community, theatre community.

Industry/Entity Type

Performing Art

Contact Information for Business Card

Owen Talvik. Pronouns: he, him, his. Contact info: (555)-310-7826, Owentalvik.example, owentalvik@mailbox.example. Talent representation: Brindlecove Talent Agency. Social Media: Facebook page, twitter and instagram: @OwenTalvikPlays. Company Member of Harrowgate Theatre Company.

Font styles to use
Serif
Decorative

Colors

Designer to choose colors to be used in the design.

Requirements
Must have
• Headshot photo, name, tagline, preferred pronouns, contact info, Social media handle, talent agency logo, harrowgate theatre company logo. Both logos should be smaller than my name. Under or near Harrowgate logo, it should say "Company Member"
Nice to have
• I would like to have the photo, my name, tagline, and maybe pronouns on one side, and all contact info, and social media, and talent agency logo on the other. I would like the style to reflect my type which is a little more serious and somewhat darker, and definitely not comedic.
Should not have
• No extraneous theatre lights, camera, or film, etc. clip art or photos. Use solid backgrounds or photos provided.

```html
<!DOCTYPE html>
<html lang="en">
<head>
<meta charset="utf-8">
<title>Owen Talvik – Business Cards</title>
<link rel="stylesheet" href="https://fonts.googleapis.com/css2?family=Oswald:wght@700&family=Open+Sans:wght@300;400&display=swap">
<style>
  :root {
    --stage: #d8d4cc;
    --card-dark: #141414;
    --card-dark-2: #262626;
    --photo-grey-1: #8a8a8a;
    --photo-grey-2: #4a4a4a;
    --photo-blue-1: #9cc3d2;
    --photo-blue-2: #5f8ea1;
    --photo-blue-3: #2e5262;
    --photo-blue-4: #1f3a46;
    --band: rgba(28, 50, 62, 0.75);
    --ink-light: #ffffff;
    --ink-soft: #d2d2d2;
    --rule: rgba(255, 255, 255, 0.5);
  }
  * { box-sizing: border-box; margin: 0; padding: 0; }
  html, body { width: 771px; height: 1200px; overflow: hidden; }
  body {
    position: relative;
    background: var(--stage);
    font-family: "Open Sans", Arial, sans-serif;
    color: var(--ink-light);
  }
  .card {
    position: absolute;
    left: 230px;
    width: 310px;
    height: 540px;
    border-radius: 16px;
    overflow: hidden;
    box-shadow: 0 10px 24px rgba(0, 0, 0, 0.28);
  }
  .card--contact { top: 30px; background: linear-gradient(180deg, var(--card-dark-2), var(--card-dark)); }
  .card--headshot { top: 630px; }

  /* shared identity type */
  .identity__name {
    font-family: "Oswald", Impact, sans-serif; font-weight: 700;
    font-size: 36px; letter-spacing: 1px; text-transform: uppercase; line-height: 1.1;
  }
  .identity__tagline { font-weight: 300; font-size: 14px; color: var(--ink-soft); line-height: 1.3; }
  .identity__pronouns { font-weight: 300; font-size: 12px; color: var(--ink-soft); letter-spacing: 1px; margin-top: 2px; }

  /* contact side */
  .contact__photo {
    position: absolute; top: 0; left: 60px; right: 0; height: 210px;
    background:
      radial-gradient(ellipse 60% 70% at 62% 42%, var(--photo-grey-1) 0%, var(--photo-grey-2) 55%, rgba(38,38,38,0) 100%);
  }
  .identity { position: absolute; top: 112px; left: 0; right: 0; text-align: center; }

  .contact-list { position: absolute; top: 194px; left: 26px; right: 26px; list-style: none; }
  .contact-list__item {
    display: flex; align-items: center; height: 34px;
    border-bottom: 1px solid var(--rule);
    font-size: 13px;
  }
  .contact-list__item--phone { font-size: 15px; }
  .contact-list__icon { width: 30px; height: 18px; flex: none; display: flex; align-items: center; }
  .contact-list__text { flex: 1; text-align: center; }

  .affiliation { position: absolute; left: 26px; right: 26px; }
  .affiliation--agency { top: 412px; }
  .affiliation--company { top: 466px; }
  .affiliation__label { font-size: 12px; color: var(--ink-soft); }
  .affiliation__name {
    display: flex; align-items: center; gap: 7px; justify-content: flex-end;
    margin-top: 4px; font-size: 14px; color: var(--ink-light);
  }
  .affiliation__dot { width: 9px; height: 9px; border-radius: 50%; background: var(--photo-blue-1); flex: none; }
  .affiliation__square { width: 9px; height: 9px; background: var(--photo-blue-1); flex: none; }

  /* headshot side */
  .headshot__photo {
    position: absolute; inset: 0;
    background:
      radial-gradient(ellipse 45% 35% at 66% 30%, var(--photo-blue-1) 0%, rgba(156,195,210,0) 100%),
      linear-gradient(90deg, var(--photo-blue-3) 0%, var(--photo-blue-2) 30%, var(--photo-blue-2) 70%, var(--photo-blue-3) 100%),
      var(--photo-blue-2);
  }
  .headshot__shade {
    position: absolute; left: 0; right: 0; bottom: 0; height: 260px;
    background: linear-gradient(180deg, rgba(31,58,70,0) 0%, var(--photo-blue-4) 100%);
  }
  .headshot__band {
    position: absolute; left: 0; right: 0; top: 312px; height: 100px;
    background: var(--band);
    border-top: 1px solid var(--rule); border-bottom: 1px solid var(--rule);
    display: flex; flex-direction: column; justify-content: center; align-items: center;
    text-align: center;
  }
</style>
</head>
<body>

<section class="card card--contact">
  <div class="contact__photo" role="img" aria-label="Greyscale headshot photo of the actor, fading into the dark card"></div>
  <div class="identity">
    <h1 class="identity__name">Owen Talvik</h1>
    <p class="identity__tagline">Actor, storyteller, theatre maker</p>
  </div>
  <ul class="contact-list">
    <li class="contact-list__item contact-list__item--phone">
      <span class="contact-list__icon"><svg width="18" height="16" viewBox="0 0 18 16"><path d="M2 5c0-2 3-3 7-3s7 1 7 3v1h-4V4.5H6V6H2z M4 7h10l2 7H2z" fill="#fff"/><circle cx="9" cy="10.5" r="2" fill="#161616"/></svg></span>
      <span class="contact-list__text">(555)-310-7826</span>
    </li>
    <li class="contact-list__item">
      <span class="contact-list__icon"><svg width="18" height="13" viewBox="0 0 18 13"><rect x="0.5" y="0.5" width="17" height="12" fill="none" stroke="#fff"/><path d="M0.5 0.5L9 7l8.5-6.5" fill="none" stroke="#fff"/></svg></span>
      <span class="contact-list__text">owentalvik@mailbox.example</span>
    </li>
    <li class="contact-list__item">
      <span class="contact-list__icon"><svg width="17" height="17" viewBox="0 0 17 17" fill="none" stroke="#fff"><circle cx="8.5" cy="8.5" r="7.5"/><ellipse cx="8.5" cy="8.5" rx="3.5" ry="7.5"/><path d="M1 8.5h15M2.5 4.5h12M2.5 12.5h12"/></svg></span>
      <span class="contact-list__text">Owentalvik.example</span>
    </li>
    <li class="contact-list__item">
      <span class="contact-list__icon"><svg width="14" height="14" viewBox="0 0 14 14"><circle cx="7" cy="7" r="6" fill="none" stroke="#fff" stroke-width="1.5"/></svg></span>
      <span class="contact-list__text">@OwenTalvikPlays</span>
    </li>
    <li class="contact-list__item">
      <span class="contact-list__icon"><svg width="14" height="14" viewBox="0 0 14 14"><circle cx="7" cy="7" r="6" fill="none" stroke="#fff" stroke-width="1.5"/></svg></span>
      <span class="contact-list__text">@OwenTalvikPlays</span>
    </li>
    <li class="contact-list__item">
      <span class="contact-list__icon"><svg width="14" height="14" viewBox="0 0 14 14"><circle cx="7" cy="7" r="6" fill="none" stroke="#fff" stroke-width="1.5"/></svg></span>
      <span class="contact-list__text">@OwenTalvikPlays</span>
    </li>
  </ul>
  <div class="affiliation affiliation--agency">
    <p class="affiliation__label">Talent representation</p>
    <p class="affiliation__name"><span class="affiliation__dot"></span><span>Brindlecove Talent Agency</span></p>
  </div>
  <div class="affiliation affiliation--company">
    <p class="affiliation__label">Company Member</p>
    <p class="affiliation__name"><span class="affiliation__square"></span><span>Harrowgate Theatre Company</span></p>
  </div>
</section>

<section class="card card--headshot">
  <div class="headshot__photo" role="img" aria-label="Blue-toned headshot photo of the actor"></div>
  <div class="headshot__shade"></div>
  <div class="headshot__band">
    <h2 class="identity__name">Owen Talvik</h2>
    <p class="identity__tagline">Actor, storyteller, theatre maker</p>
    <p class="identity__pronouns">he / him / his</p>
  </div>
</section>

</body>
</html>
```